Website For Custom Home Builder

-Very elegant and simple design as I am a high end custom home builder.
-I build homes $2 million to $10 million range so the website needs to reflect the level of home that I build.
-Attached are photos of homes I have built to use as well as my logo.
-I need final design to be in layered format so my local guy can edit if he needs to.

3 Page Design
1. HomePage:
-logo, some photos,
-“Building beautiful custom homes in Indianapolis for over 20 years”
2. AboutPage:
-Wade Holloran has been building stunning custom homes in the Indianpolis area for over 20 years. As a small boutique building company we only build a handful of homes a year in order to offer our clients the personal attention that their homes deserve. It's this attention to detail that makes our client experience and final product something special and unique.
- family photo
3. ContactPage:
-office photo
-317-552-7190
-wade@whcrafted.com
-415 North Fernmill Rd, Suite 308, Carmel IN 46033

Target Market(s)

Very high end clients looking to build $2 million to $10 million homes.

Industry/Entity Type

Residential high end custom home builder/construction

Coding

Coded - Design and coding required

Number of Pages Required

3 page

Requirements
Must have
• Very simple and elegant design that represents the high end homes that I build.
Nice to have
Should not have
• Should NOT have a lot of clutter or be a very busy page from a design perspective.

```html
<!DOCTYPE html>
<html lang="en">
<head>
<meta charset="utf-8">
<title>Wade Holloran Custom Homes</title>
<link rel="stylesheet" href="https://fonts.googleapis.com/css2?family=Outfit:wght@300;400;600;700&display=swap">
<style>
:root{
  --brown:#a3581b;
  --ink:#222;
  --text:#3a3a3a;
  --blush:#f6ece7;
  --sand:#efe1d4;
  --paper:#fafafa;
  --line:#cfcfcf;
  --white:#fff;
}
*{margin:0;padding:0;box-sizing:border-box}
html,body{width:792px;height:1200px;overflow:hidden;background:var(--white)}
body{position:relative;font-family:"Outfit",sans-serif;color:var(--text)}
.abs{position:absolute}

/* header */
.brand{left:79px;top:22px;display:flex;align-items:center;gap:7px;font-weight:400;font-size:17px;color:var(--ink);letter-spacing:.3px}
.brand-mark{width:12px;height:12px;background:var(--brown)}
.nav{top:27px;left:333px;display:flex;gap:38px;font-size:8px;letter-spacing:.4px;color:var(--ink)}
.nav .active{color:var(--brown)}
.call{left:565px;top:0;width:227px;height:69px;background:var(--brown);color:var(--white);padding:16px 0 0 20px}
.call-label{font-size:11.5px;font-weight:300;letter-spacing:.6px;display:flex;align-items:center;gap:8px}
.call-number{font-size:17.5px;font-weight:700;letter-spacing:.8px;margin-top:2px}

/* hero */
.hero{left:0;top:69px;width:792px;height:377px;background:linear-gradient(180deg,#3a3129 0%,#6e5233 28%,#2f2c25 55%,#26323a 80%,#3b3326 100%)}
.hero-shade{left:0;top:69px;width:792px;height:377px;background:rgba(0,0,0,.18)}
.hero-title{left:0;top:198px;width:792px;text-align:center;color:var(--white);font-weight:700;font-size:26.5px;line-height:34px;letter-spacing:-.2px}
.hero-btn{left:351px;top:285px;width:89px;height:25px;border:1px solid var(--white);color:var(--white);font-size:8px;display:flex;align-items:center;justify-content:center;letter-spacing:.3px}
.arrow{top:245px;width:25px;height:25px;display:flex;align-items:center;justify-content:center}
.arrow.prev{left:27px;border:1px solid var(--white)}
.arrow.next{left:740px;background:#eeeef2}
.scroll{left:389px;top:402px;width:15px;height:24px;border:1px solid var(--white);border-radius:8px}
.scroll::after{content:"";position:absolute;left:6px;top:5px;width:2px;height:5px;background:var(--white);border-radius:1px}

/* about */
.about-sand{left:434px;top:446px;width:358px;height:338px;background:var(--sand)}
.about-band{left:0;top:530px;width:733px;height:323px;background:var(--blush)}
.about-photo{left:455px;top:510px;width:258px;height:294px;background:linear-gradient(180deg,#c9ced2 0%,#d8d8d4 35%,#b9bcb5 60%,#6f8356 80%,#5d7448 100%)}
.about-square{left:79px;top:565px;width:14px;height:14px;background:var(--brown)}
.eyebrow{color:var(--brown);font-size:12.5px;font-weight:300;letter-spacing:.3px}
.about-eyebrow{left:79px;top:610px}
.heading{color:var(--ink);font-weight:600;font-size:26.5px;letter-spacing:-.2px}
.about-heading{left:79px;top:627px}
.about-copy{left:79px;top:669px;width:306px;font-size:8.6px;line-height:14px;font-weight:300;color:var(--text)}
.btn-fill{left:79px;top:770px;width:79px;height:25px;background:var(--brown);color:var(--white);font-size:8px;display:flex;align-items:center;justify-content:center;letter-spacing:.3px}

/* contact */
.contact{left:0;top:853px;width:792px;height:317px;background:var(--paper)}
.contact-eyebrow{left:0;top:900px;width:792px;text-align:center}
.contact-heading{left:0;top:917px;width:792px;text-align:center}
.field{height:25px;border:1px solid var(--line);background:var(--white);font-size:8px;color:#555;padding:7px 9px;font-weight:300;letter-spacing:.2px}
.col-a{left:153px;width:235px}
.col-b{left:403px;width:235px}
.row-1{top:962px}
.row-2{top:997px}
.message{left:153px;top:1032px;width:485px;height:49px}
.btn-line{left:357px;top:1096px;width:78px;height:25px;border:1px solid var(--brown);color:var(--brown);font-size:8px;display:flex;align-items:center;justify-content:center;letter-spacing:.3px;background:var(--white)}

/* footer */
.footer{left:0;top:1170px;width:792px;height:30px;background:var(--brown);color:var(--white);font-size:7px;font-weight:300}
.footer span{position:absolute;top:11px}
.footer b{font-weight:700}
.footer u{text-decoration:underline}
</style>
</head>
<body>

<header>
  <div class="abs brand"><span class="brand-mark"></span>WADE HOLLORAN</div>
  <nav class="abs nav">
    <span class="active">HOME</span>
    <span>ABOUT US</span>
    <span>CONTACT US</span>
  </nav>
  <div class="abs call">
    <div class="call-label">CALL US
      <svg width="13" height="13" viewBox="0 0 24 24" fill="none" stroke="#fff" stroke-width="2"><path d="M5 3h4l2 5-3 2a12 12 0 0 0 6 6l2-3 5 2v4a2 2 0 0 1-2 2A17 17 0 0 1 3 5a2 2 0 0 1 2-2z"/></svg>
    </div>
    <div class="call-number">317-552-7190</div>
  </div>
</header>

<section>
  <div class="abs hero" role="img" aria-label="Evening view of a luxury stone custom home with pool and terrace"></div>
  <div class="abs hero-shade"></div>
  <h1 class="abs hero-title">BUILDING BEAUTIFUL CUSTOM HOMES IN<br>INDIANAPOLIS FOR OVER 20 YEARS</h1>
  <div class="abs hero-btn">CONTACT US</div>
  <div class="abs arrow prev"><svg width="8" height="10" viewBox="0 0 8 10"><path d="M6 1L2 5l4 4" fill="none" stroke="#fff" stroke-width="1.2"/></svg></div>
  <div class="abs arrow next"><svg width="8" height="10" viewBox="0 0 8 10"><path d="M2 1l4 4-4 4" fill="none" stroke="#333" stroke-width="1.2"/></svg></div>
  <div class="abs scroll"></div>
</section>

<section>
  <div class="abs about-sand"></div>
  <div class="abs about-band"></div>
  <div class="abs about-photo" role="img" aria-label="Family standing on the lawn in front of a white custom home"></div>
  <div class="abs about-square"></div>
  <div class="abs eyebrow about-eyebrow">WELCOME TO</div>
  <h2 class="abs heading about-heading">WADE HOLLORAN</h2>
  <p class="abs about-copy">Wade Holloran has been building stunning custom homes in the Indianpolis area for over 20 years. As a small boutique building company we only build a handful of homes a year in order to offer our clients the personal attention that their homes deserve. It's this attention to detail that makes our client experience and final product something special and unique.</p>
  <div class="abs btn-fill">ABOUT US</div>
</section>

<section>
  <div class="abs contact"></div>
  <div class="abs eyebrow contact-eyebrow">ENQUIRY NOW!</div>
  <h2 class="abs heading contact-heading">CONTACT US</h2>
  <div class="abs field col-a row-1">Full Name</div>
  <div class="abs field col-b row-1">Email Address*</div>
  <div class="abs field col-a row-2">Phone Number*</div>
  <div class="abs field col-b row-2">Subject</div>
  <div class="abs field message">Messages...</div>
  <div class="abs btn-line">SUBMIT</div>
</section>

<footer class="abs footer">
  <span style="left:79px"><b>E.:</b> <u>wade@whcrafted.com</u></span>
  <span style="left:287px"><b>ADDRESS:</b> 415 North Fernmill Rd, Suite 308, Carmel IN 46033</span>
  <span style="left:558px">© Copyright <u>Wade Holloran.</u> All Right Reserved.</span>
</footer>

</body>
</html>
```